High-end residential home builder needs a business card design

We need a new business card design for a small residential construction company based in Boise, Idaho. We specialize in building custom high-end homes and remodels, with a focus on great design and craftsmanship.

We would like to use our current logo, but open to new color suggestions.
Just looking for a clean, sharp, modern design that looks high-end.

Target Market(s)

Upscale clientele

Industry/Entity Type

Contractor

Contact Information for Business Card

Company: Stonefield Custom Builders
Name: Marcus Tilley
Phone number: 208 367 4120
Email: MarcusTilleySCB@mailbox-example.com
Website: Stonefieldcustombuilders-example.com

Font styles to use
Serif
Sans Serif

Requirements
Must have
• Company Logo
Company name
My name
My phone number
My email
Company website
Nice to have
• I have attached a few photos of cards that I really like.

```html
<!DOCTYPE html>
<html lang="en">
<head>
<meta charset="utf-8">
<title>Stonefield Custom Builders – Business Card</title>
<link rel="stylesheet" href="https://fonts.googleapis.com/css2?family=Lato:wght@400;700&display=swap">
<style>
  :root {
    --brown: #311c0a;
    --white: #ffffff;
    --page: #ececec;
    --ink: #2a1a0c;
    --accent: #e39a3c;
  }
  * { margin: 0; padding: 0; box-sizing: border-box; }
  html, body {
    width: 1200px;
    height: 840px;
    overflow: hidden;
    background: var(--page);
    font-family: "Lato", sans-serif;
  }
  .canvas { position: relative; width: 1200px; height: 840px; }
  .card {
    position: absolute;
    top: 282px;
    width: 482px;
    height: 275px;
    border-radius: 26px;
    overflow: hidden;
  }
  .card-front { left: 106px; background: var(--brown); color: var(--white); }
  .card-back { left: 614px; background: var(--white); color: var(--ink); }

  .brand {
    position: absolute;
    display: flex;
    flex-direction: column;
    align-items: center;
    gap: 12px;
  }
  .brand-mark {
    width: 46px;
    height: 46px;
    border: 2px solid currentColor;
  }
  .brand-name {
    font-weight: 700;
    font-size: 13px;
    letter-spacing: 4px;
    text-transform: uppercase;
    text-align: center;
    line-height: 1.5;
  }
  .card-front .brand { left: 0; right: 0; top: 66px; }
  .card-back .brand { left: 20px; width: 180px; top: 76px; color: var(--ink); }
  .card-back .brand-name { font-size: 11px; letter-spacing: 3px; }

  .front-web {
    position: absolute;
    left: 0; right: 0;
    top: 236px;
    text-align: center;
    font-size: 15px;
  }

  .company-title {
    position: absolute;
    right: 24px;
    top: 18px;
    font-weight: 700;
    font-size: 17px;
  }
  .person {
    position: absolute;
    left: 228px;
    top: 108px;
    display: flex;
    align-items: center;
    gap: 12px;
  }
  .person-name { font-weight: 700; font-size: 22px; }
  .contacts {
    position: absolute;
    left: 234px;
    top: 158px;
    list-style: none;
  }
  .contacts::before {
    content: "";
    position: absolute;
    left: 10px;
    top: 14px;
    bottom: 14px;
    width: 1px;
    background: var(--brown);
  }
  .contact {
    position: relative;
    display: flex;
    align-items: center;
    gap: 16px;
    height: 31px;
    font-size: 10.5px;
  }
  .hex-icon { display: block; flex: none; }
</style>
</head>
<body>
<main class="canvas">

  <section class="card card-front" aria-label="Card front">
    <div class="brand">
      <span class="brand-mark"></span>
      <span class="brand-name">Stonefield<br>Custom Builders</span>
    </div>
    <p class="front-web">Stonefieldcustombuilders-example.com</p>
  </section>

  <section class="card card-back" aria-label="Card back">
    <h1 class="company-title">Stonefield Custom Builders</h1>

    <div class="brand">
      <span class="brand-mark"></span>
      <span class="brand-name">Stonefield<br>Custom Builders</span>
    </div>

    <div class="person">
      <svg class="hex-icon" width="32" height="36" viewBox="0 0 32 36" aria-hidden="true">
        <polygon points="16,0 32,9 32,27 16,36 0,27 0,9" fill="var(--brown)"/>
        <circle cx="16" cy="13" r="4.5" fill="var(--white)"/>
        <path d="M8 26 q0 -7 8 -7 q8 0 8 7 z" fill="var(--white)"/>
      </svg>
      <span class="person-name">Marcus Tilley</span>
    </div>

    <ul class="contacts">
      <li class="contact">
        <svg class="hex-icon" width="21" height="24" viewBox="0 0 21 24" aria-hidden="true">
          <polygon points="10.5,0 21,6 21,18 10.5,24 0,18 0,6" fill="var(--brown)"/>
          <path d="M6.5 7 l2 -0.5 1 2.5 -1.2 1 q1 2 2.7 2.7 l1 -1.2 2.5 1 -0.5 2 q-4 0.5 -6.5 -3 q-1.8 -2.4 -1 -4.5z" fill="var(--white)"/>
        </svg>
        <span>208 367 4120</span>
      </li>
      <li class="contact">
        <svg class="hex-icon" width="21" height="24" viewBox="0 0 21 24" aria-hidden="true">
          <polygon points="10.5,0 21,6 21,18 10.5,24 0,18 0,6" fill="var(--brown)"/>
          <rect x="5" y="8" width="11" height="8" rx="1" fill="var(--white)"/>
          <path d="M5 8.5 l5.5 4 5.5 -4" fill="none" stroke="var(--brown)" stroke-width="1"/>
        </svg>
        <span>MarcusTilleySCB@mailbox-example.com</span>
      </li>
      <li class="contact">
        <svg class="hex-icon" width="21" height="24" viewBox="0 0 21 24" aria-hidden="true">
          <polygon points="10.5,0 21,6 21,18 10.5,24 0,18 0,6" fill="var(--brown)"/>
          <g fill="none" stroke="var(--white)" stroke-width="1.6" stroke-linecap="round">
            <path d="M9.5 10.5 l2.2 -2.2 a2 2 0 0 1 2.8 2.8 l-2.2 2.2"/>
            <path d="M11.5 13.5 l-2.2 2.2 a2 2 0 0 1 -2.8 -2.8 l2.2 -2.2"/>
            <path d="M9 14.5 l3 -3"/>
          </g>
        </svg>
        <span>Stonefieldcustombuilders-example.com</span>
      </li>
    </ul>
  </section>

</main>
</body>
</html>
```